Catalogue Design Project

I need a professional catalogue design for a Luxury Pet company. We are retail, wholesale and drop ship.
Our company name is Mabel & Finn we are the leading supplier of Luxury pet supplies. Our slogan is: Luxury lifestyle for our four legged friends.
My company colour is pantone 318c, lighter and more blue than used on our website www.mabelandfinn.com.au
We are looking for very luxury, boutique, a bit like harlow & vane, sophisticated. The catalogue needs a cover, a index, and photo page graphic designs for each category.
Also needed is a excel spreadsheet layout for pricelists, and a order form design.
A printable and PDF format will be required, as well as all graphic design. It initial catalogue will be approx 50pages.
Updates

Please note for the right design I am prepared to pay up to AUD$2000.

Target Market(s)

younger successful audience not yet with kids who love their pets

Industry/Entity Type

Pet

Requirements
Must have
• A front cover design
A Back Cover Design
A index page design
A category photo/graphic design page for each category
A uniform design and feel across the catalogue

```html
<!DOCTYPE html>
<html lang="en">
<head>
<meta charset="utf-8">
<title>Mabel &amp; Finn Catalogue – Pages 3–4</title>
<link rel="stylesheet" href="https://fonts.googleapis.com/css2?family=Tinos:wght@400;700&display=swap">
<style>
  :root {
    --brand-blue: #9fcbd4;
    --brand-blue-text: #8cc3cd;
    --ink: #4a4a4a;
    --paper: #ffffff;
    --backdrop: #ece9e4;
    --sweater-red: #c4262e;
    --sweater-cream: #f1ece4;
    --coat-grey: #3a3d44;
    --coat-fur: #1c1c1e;
    --pup-white: #e9e7e2;
  }
  * { box-sizing: border-box; margin: 0; padding: 0; }
  html, body { width: 1200px; height: 1000px; overflow: hidden; }
  body {
    background: var(--backdrop);
    font-family: "Tinos", "Times New Roman", serif;
    color: var(--ink);
    position: relative;
  }
  .spread {
    position: absolute; left: 27px; top: 103px;
    width: 1146px; height: 810px;
    background: var(--paper);
    overflow: hidden;
  }
  .abs { position: absolute; }
  .section-label {
    font-size: 8px; letter-spacing: 0.3px; color: var(--brand-blue-text); top: 39px;
  }
  .title-band {
    top: 77px; height: 67px; background: var(--brand-blue); color: #fff;
    padding: 7px 0 0 90px; text-transform: uppercase;
  }
  .title-band h2 { font-weight: 400; font-size: 16.5px; line-height: 19px; }
  .title-band p { font-size: 10.5px; line-height: 12px; }
  .title-band.right { padding-left: 22px; }
  .description { font-size: 10.8px; line-height: 14px; text-transform: uppercase; }
  .description p + p { margin-top: 14px; }
  .sizes { font-size: 10.8px; line-height: 14px; }
  .price { font-size: 21px; font-weight: 700; color: var(--brand-blue-text); }
  .was-price { font-size: 10px; text-decoration: line-through; }
  .sweater-photo {
    background: linear-gradient(180deg, var(--sweater-red) 0%, #b21f28 70%, var(--sweater-cream) 100%);
    border-radius: 30px 30px 40px 40px;
  }
  .coat-photo {
    background: linear-gradient(180deg, var(--coat-grey) 0%, var(--coat-fur) 55%, #6b6a68 72%, var(--pup-white) 100%);
    border-radius: 36px;
  }
  .fit-guide {
    background: linear-gradient(135deg, #eef7f9, #d5ebef);
    border-radius: 40px 40px 20px 20px;
  }
  .size-chart { font-size: 4px; line-height: 4.6px; }
  .size-chart caption { font-weight: 700; text-align: left; }
  .size-chart table { border-collapse: collapse; width: 100%; }
  .size-chart th, .size-chart td { border: 0.5px solid #333; padding: 0 1px; text-align: left; }
  .info-block { font-size: 9.4px; line-height: 11.6px; text-transform: uppercase; }
  .info-block .tagline { background: var(--brand-blue); color: var(--ink); padding: 0 2px; display: inline-block; }
  .info-block p + p { margin-top: 11px; }
  .page-rule { top: 742px; width: 1px; height: 68px; background: var(--brand-blue); }
  .page-number { top: 771px; font-size: 15px; color: var(--brand-blue-text); }
  .slogan-box {
    top: 757px; background: var(--brand-blue); color: #fff;
    font-size: 12.5px; line-height: 15px; padding: 1px 4px; text-transform: uppercase;
    white-space: nowrap;
  }
</style>
</head>
<body>
<main class="spread">

  <section class="page page-left">
    <div class="abs section-label" style="left:89px;">OCASSIONS/EVENTS</div>
    <header class="abs title-band" style="left:0;width:313px;">
      <h2>Christmas Snowflake<br>&amp; Pom Pom Sweater</h2>
      <p>Hand Knitted Dog Sweater</p>
    </header>
    <div class="abs description" style="left:90px;top:163px;width:440px;">
      <p>Product Description<br>Christmas Snowflake &amp; Pom Pom Pet Sweater by Mabel &amp; Finn</p>
      <p>This hand knitted Christmas dog sweater will make any pet look<br>adorable this Christmas as well as being lots of fun.<br>Designed by Mabel &amp; Finn in Australia, and hand knitted<br>to the highest standards, when only the best will do to spoil<br>your pampered pooch this Christmas.</p>
    </div>
    <div class="abs sweater-photo" style="left:78px;top:305px;width:135px;height:187px;" role="img" aria-label="Red knitted Christmas dog sweater with snowflake pattern, white pom poms and fluffy trim"></div>
    <div class="abs sizes" style="left:275px;top:327px;">SIZES:<br>XS - 25CM<br>S - 30CM<br>M - 35CM<br>L - 40CM<br>XL - 45CM<br>XXL - 50CM</div>
    <div class="abs price" style="left:274px;top:436px;">$20.00</div>
    <div class="abs was-price" style="left:274px;top:462px;">$45.00</div>
    <div class="abs fit-guide" style="left:378px;top:337px;width:126px;height:86px;" role="img" aria-label="Line drawing of a small dog showing where to measure neck, length and girth"></div>
    <div class="abs size-chart" style="left:393px;top:434px;width:106px;">
      <table>
        <caption>Apparel Size Chart</caption>
        <tr><th>Size</th><th>Length</th><th>Neck</th><th>Girth</th></tr>
        <tr><td>XSmall</td><td>7-9"</td><td>7-9"</td><td>11-14"</td></tr>
        <tr><td>Small</td><td>9-11"</td><td>9-11"</td><td>14-17"</td></tr>
        <tr><td>Medium</td><td>11-13"</td><td>11-13"</td><td>17-19"</td></tr>
        <tr><td>MMed</td><td>13-15"</td><td>12-14"</td><td>19-20"</td></tr>
        <tr><td>Large</td><td>15-17"</td><td>13-15"</td><td>20-22"</td></tr>
        <tr><td>XLarge</td><td>17-19"</td><td>14-16"</td><td>22-24"</td></tr>
      </table>
    </div>
    <div class="abs info-block" style="left:90px;top:611px;width:460px;">
      <span class="tagline">Designer Pet Furniture | Pet Beds | Dog Beds | Cat Beds</span>
      <p>Designer pet beds are really the latest thing these days for dog and cat lovers.</p>
      <p>Designer pet furniture is special.&nbsp; The quality of the pet beds is exceptional<br>with only the finest pet bedding fabric and materials used in both dog beds<br>and cat beds. Enjoy your journey through our exciting range of pet beds<br>in assorted styles and colours and check out all the designer dog beds<br>and cat beds created with strength, style and comfort.</p>
    </div>
    <div class="abs page-rule" style="left:89px;"></div>
    <div class="abs page-number" style="left:40px;">3</div>
    <div class="abs slogan-box" style="left:365px;">Luxury Lifestyle for<br>our four legged friends.</div>
  </section>

  <section class="page page-right">
    <div class="abs section-label" style="left:866px;">COATS, JACKETS &amp; T-SHIRTS</div>
    <header class="abs title-band right" style="left:843px;width:303px;">
      <h2>Velo London Coat</h2>
      <p>Hand Knitted Dog Sweater</p>
    </header>
    <div class="abs coat-photo" style="left:580px;top:130px;width:232px;height:368px;" role="img" aria-label="Charcoal dog coat with black faux fur trim and buckled strap, shown on its own and worn by a small white dog"></div>
    <div class="abs sizes" style="left:828px;top:344px;">SIZES:<br>XS - ONLY 1 LEFT<br>S - ONLY 2 LEFT<br>M - ONLY 2 LEFT<br>L - ONLY 1 LEFT</div>
    <div class="abs price" style="left:834px;top:436px;">$40.00</div>
    <div class="abs was-price" style="left:834px;top:462px;">$45.00</div>
    <div class="abs fit-guide" style="left:938px;top:337px;width:126px;height:86px;" role="img" aria-label="Line drawing of a small dog showing where to measure neck, length and girth"></div>
    <div class="abs size-chart" style="left:953px;top:434px;width:106px;">
      <table>
        <caption>Apparel Size Chart</caption>
        <tr><th>Size</th><th>Length</th><th>Neck</th><th>Girth</th></tr>
        <tr><td>XSmall</td><td>7-9"</td><td>7-9"</td><td>11-14"</td></tr>
        <tr><td>Small</td><td>9-11"</td><td>9-11"</td><td>14-17"</td></tr>
        <tr><td>Medium</td><td>11-13"</td><td>11-13"</td><td>17-19"</td></tr>
        <tr><td>MMed</td><td>13-15"</td><td>12-14"</td><td>19-20"</td></tr>
        <tr><td>Large</td><td>15-17"</td><td>13-15"</td><td>20-22"</td></tr>
        <tr><td>XLarge</td><td>17-19"</td><td>14-16"</td><td>22-24"</td></tr>
      </table>
    </div>
    <div class="abs info-block" style="left:651px;top:611px;width:460px;">
      <span class="tagline">Designer Pet Furniture | Pet Beds | Dog Beds | Cat Beds</span>
      <p>Designer pet beds are really the latest thing these days for dog and cat lovers.</p>
      <p>Designer pet furniture is special.&nbsp; The quality of the pet beds is exceptional<br>with only the finest pet bedding fabric and materials used in both dog beds<br>and cat beds. Enjoy your journey through our exciting range of pet beds<br>in assorted styles and colours and check out all the designer dog beds<br>and cat beds created with strength, style and comfort.</p>
    </div>
    <div class="abs slogan-box" style="left:595px;">Luxury Lifestyle for<br>our four legged friends.</div>
    <div class="abs page-rule" style="left:1058px;"></div>
    <div class="abs page-number" style="left:1097px;">4</div>
  </section>

</main>
</body>
</html>
```